Automotive Locksmiith company needs a website design and mobile website

We need a website design and a mobile design for an automotive locksmith company called Halvern Keyworks LLC.We are based in the center of the Dallas-Fort Worth Metroplex. We have a website that was directed more towards the towing services we also offer. We would like to have it more towards our locksmith products. Our main services include:
Auto keys duplication
Cutting of new car keys
Car Lockouts
Laser key replacement
Cutting keys by code
Broken key extractions
Production of transponder keys
Key fob programming
Door lock repairs
Ignition repairs/replacement
We work on 95% of the automotive market that includes Vorla, Tessin, QRT, Pembrook, Marquenne, Dunmoral, Brask, VX, Sorvalo, Kelto, Zephrane, Oru, Hadley, Norax, Tabori, Valdrenne, Quillon, Pipo, Runel Okarawe , Brevik, Solumé, Drennhofer, Kestra.
We are one of the most affordable services in the DFW area . Our prices for transponder copies start at $35 per key. We provide services for high-end vehicles also as QRT and Valdrenne. We can program the new proximity keys for Tabori Vehicles 2013-up. We also work on the new Pell Vehicles 20-13 and up including the Pell Arden head remote key.
We would like to have a similar style to the website we already have with the option to schedule an appointment on the mobile website. This mobile application will deliver an email when a new customer is requiring the service. It will ask for Year, Make, Model , Service to be performed( Key copy, Lockout, Lost Key, Change Ignition lock, change door lock, Other services.) Description of the service to be performed, Address, Select time of service.
Our current website is halvernkeyworks.example

Reason: Need pictures of webpages inside design (about us , location etc) and mobile pictures( how website looks in Quorra / android)

Automotive

• check word attachment

```html
<!DOCTYPE html>
<html lang="en">
<head>
<meta charset="utf-8">
<title>Halvern Keyworks LLC</title>
<link href="https://fonts.googleapis.com/css2?family=Roboto:wght@400;500;700&display=swap" rel="stylesheet">
<style>
:root{
  --teal:#0aa2c6;
  --navy:#0b4874;
  --ink:#333;
  --muted:#555;
  --line:#e2e2e2;
  --chip:#ededed;
  --navbg:#f3f3f3;
  --foot-a:#0c4a79;
  --foot-b:#0b5f8d;
}
*{box-sizing:border-box;margin:0;padding:0}
html,body{width:1200px;height:2192px;overflow:hidden;background:#fff;font-family:'Roboto',Arial,sans-serif;color:var(--ink)}
.wrap{width:941px;margin-left:130px;position:relative}
/* header */
.site-header{height:127px;position:relative}
.brand{position:absolute;left:131px;top:58px;display:flex;align-items:center;gap:10px}
.brand-mark{width:26px;height:26px;background:var(--teal)}
.brand-name{font-size:24px;font-weight:500;color:#3f6b86;letter-spacing:-.3px}
.contact{position:absolute;right:129px;text-align:right;font-size:12px;color:#444;display:flex;align-items:center;gap:6px}
.contact.tel{top:38px}
.contact.tel b{font-weight:400;font-size:17px;color:var(--teal)}
.contact.addr{top:80px;letter-spacing:.2px}
/* nav */
.main-nav{height:51px;background:var(--navbg)}
.main-nav ul{list-style:none;display:flex;height:51px;align-items:center;font-size:14px;color:#333}
.main-nav li{height:51px;display:flex;align-items:center}
.main-nav li.active{background:var(--teal);color:#fff;width:95px;justify-content:center;font-weight:500;margin-right:30px}
.main-nav li+li:not(.active){margin-right:0}
.main-nav ul li:nth-child(n+2){flex:1;justify-content:center}
/* hero */
.hero{height:576px;position:relative;overflow:hidden}
.hero-photo{position:absolute;inset:0;background:linear-gradient(100deg,#b7bcbf 0%,#6d6f73 18%,#2b2d32 38%,#3a4456 52%,#c9ccd0 70%,#b5b9bc 100%)}
.arrow{position:absolute;top:453px;width:42px;height:42px}
.arrow.prev{left:99px}.arrow.next{left:1087px}
.caption{position:absolute;left:150px;background:rgba(40,48,70,.82);color:#fff;font-size:23px;padding:0 17px;height:35px;line-height:35px;letter-spacing:.3px}
.caption.one{top:372px}.caption.two{top:427px}
.booking{position:absolute;left:738px;top:31px;width:301px;height:519px;background:#fff;border:1px solid #ddd;box-shadow:0 1px 4px rgba(0,0,0,.2);padding:0 20px}
.booking h2{font-weight:400;font-size:19px;color:var(--navy);text-align:center;padding-top:23px;padding-bottom:12px;border-bottom:1px solid var(--line);margin:0 10px 18px}
.field{margin-bottom:19px}
.field label{display:block;font-size:11px;color:#444;letter-spacing:.3px;margin-bottom:7px}
.row{display:flex;gap:18px}
.row .field{flex:1}
.box{height:31px;border:1px solid #dcdcdc;background:#f6f6f6;font-size:11px;color:#888;padding:0 13px;display:flex;align-items:center;justify-content:space-between}
.box.input{background:#fafafa}
.box .caret{font-size:9px;color:#999}
.submit{height:32px;background:var(--teal);color:#fff;font-size:12px;font-weight:500;letter-spacing:.5px;display:flex;align-items:center;justify-content:center;gap:8px;margin-top:-4px}
/* sections */
.section-title{text-align:center;font-weight:400;font-size:29px;color:#333}
.section-title span{color:var(--teal)}
.about{padding-top:64px;text-align:center}
.about p{font-size:12.5px;line-height:22px;color:var(--muted);margin:0 auto;width:860px}
.about .lead{margin-top:20px}
.about p+p{margin-top:22px}
.btn{display:inline-block;background:var(--teal);color:#fff;font-size:13px;height:36px;line-height:36px;padding:0 24px;margin-top:30px}
.divider{border-top:1px solid var(--line)}
.about+.divider{margin-top:38px}
.services{padding-top:38px}
.service-grid{display:grid;grid-template-columns:repeat(4,221px);column-gap:19px;row-gap:22px;margin-top:24px;list-style:none}
.service-grid li{height:47px;background:var(--chip);font-size:13.5px;color:#444;display:flex;align-items:center;justify-content:center}
.service-grid li.current{background:var(--navy);color:#fff}
.services+.divider{margin-top:51px}
.news{padding-top:44px}
.news-grid{display:flex;gap:19px;margin-top:30px}
.news-card{width:301px;height:193px;border:1px solid #ddd;padding:18px 19px 0}
.news-head{display:flex;gap:26px;padding-bottom:10px;border-bottom:1px solid var(--line)}
.date{text-align:center;width:56px}
.date b{display:block;font-weight:400;font-size:19px;color:var(--navy);border-bottom:1px solid #ddd;padding-bottom:2px}
.date small{font-size:10.5px;color:#333}
.news-head h3{font-weight:400;font-size:16.5px;color:var(--navy);line-height:25px;letter-spacing:.4px}
.news-card p{font-size:12.5px;line-height:24px;color:#444;margin-top:12px}
.news-card .more{display:inline-block;background:var(--navy);color:#fff;font-size:12px;height:27px;line-height:27px;padding:0 14px;margin-top:9px}
.news+.divider{margin-top:54px}
.makes{padding-top:52px}
.makes .section-title{font-size:27px}
.make-grid{display:flex;justify-content:space-between;margin-top:32px}
.make{width:142px;height:95px;border:1px solid #ddd;display:flex;align-items:center;justify-content:center;gap:7px;font-size:18px;font-weight:700;color:#333}
.make i{width:10px;height:10px;background:#9aa3ab;display:block}
/* footer */
.site-footer{position:absolute;left:0;top:2070px;width:1200px;height:122px;background:linear-gradient(180deg,var(--foot-a),var(--foot-b))}
.foot-links{position:absolute;left:133px;top:44px;font-size:12.5px;color:#fff}
.foot-links span{margin:0 5px;color:#cfe0ee}
.copy{position:absolute;left:133px;top:75px;font-size:12.5px;color:#d8e6f1}
.social{position:absolute;right:133px;top:58px;display:flex;gap:9px}
.social i{width:28px;height:28px;border-radius:50%;background:#fff;display:block}
</style>
</head>
<body>

<header class="site-header">
  <div class="brand"><span class="brand-mark"></span><span class="brand-name">Halvern Keyworks LLC</span></div>
  <div class="contact tel">
    <svg width="11" height="11" viewBox="0 0 24 24" aria-hidden="true"><path fill="#333" d="M6.6 10.8a15 15 0 0 0 6.6 6.6l2.2-2.2c.3-.3.7-.4 1-.2 1.1.4 2.3.6 3.6.6.6 0 1 .4 1 1V20c0 .6-.4 1-1 1A17 17 0 0 1 3 4c0-.6.4-1 1-1h3.5c.6 0 1 .4 1 1 0 1.3.2 2.5.6 3.6.1.3 0 .7-.2 1z"/></svg>
    TEL: <b>555-210-4187</b>
  </div>
  <div class="contact addr">
    <svg width="10" height="13" viewBox="0 0 20 26" aria-hidden="true"><path fill="#333" d="M10 0a9 9 0 0 0-9 9c0 7 9 17 9 17s9-10 9-17a9 9 0 0 0-9-9zm0 12.5A3.5 3.5 0 1 1 10 5.5a3.5 3.5 0 0 1 0 7z"/></svg>
    1420 CORVELL AVE, DALLAS, TX 75208
  </div>
</header>

<nav class="main-nav">
  <div class="wrap">
    <ul>
      <li class="active">Home</li>
      <li>About Us</li>
      <li>Services</li>
      <li>Coverage</li>
      <li>Facility</li>
      <li>Pricing</li>
      <li>Testimonials</li>
      <li>FAQ's</li>
      <li>Contact Us</li>
    </ul>
  </div>
</nav>

<section class="hero">
  <div class="hero-photo" role="img" aria-label="Photo of a man in a dark suit holding out a car key"></div>
  <svg class="arrow prev" viewBox="0 0 42 42" aria-hidden="true"><circle cx="21" cy="21" r="19" fill="rgba(255,255,255,.25)" stroke="#fff" stroke-width="2"/><path d="M25 12 15 21l10 9" fill="none" stroke="#fff" stroke-width="3"/></svg>
  <svg class="arrow next" viewBox="0 0 42 42" aria-hidden="true"><circle cx="21" cy="21" r="19" fill="rgba(255,255,255,.25)" stroke="#fff" stroke-width="2"/><path d="M17 12l10 9-10 9" fill="none" stroke="#fff" stroke-width="3"/></svg>
  <div class="caption one">PROFESSIONAL AUTOMOTIVE</div>
  <div class="caption two">SPECIAL PRICE FOR USED CAR DEALERSHIPS!</div>

  <form class="booking">
    <h2>Call to Action</h2>
    <div class="row">
      <div class="field"><label>YEAR</label><div class="box">2001<span class="caret">▼</span></div></div>
      <div class="field"><label>MAKE</label><div class="box">QRT<span class="caret">▼</span></div></div>
    </div>
    <div class="field"><label>MODEL</label><div class="box">Vantis 012<span class="caret">▼</span></div></div>
    <div class="field"><label>SERVICE TO BE PERFORMED</label><div class="box">Key Copy<span class="caret">▼</span></div></div>
    <div class="field"><label>DESCRIPTION</label><div class="box input">Enter your Command</div></div>
    <div class="field"><label>ADDRESS</label><div class="box input">Enter your Command</div></div>
    <div class="field"><label>SELECT TIME OF SERVICE</label><div class="box input">Enter your Command</div></div>
    <div class="submit">SUBMIT
      <svg width="12" height="12" viewBox="0 0 12 12" aria-hidden="true"><circle cx="6" cy="6" r="5" fill="none" stroke="#fff"/><path d="M5 3.5 7.5 6 5 8.5" fill="none" stroke="#fff"/></svg>
    </div>
  </form>
</section>

<main class="wrap">
  <section class="about">
    <h2 class="section-title">About <span>Us</span></h2>
    <p class="lead">We are a locally owned company with over 6 years of experience in the automotive industry. We provide recovery services and automotive locksmith services to the Dallas Ft-Worth Area.</p>
    <p>Our main goal is to provide unmatched customer service both to the client and your customer. You will appreciate the value of our professional approach to all your automotive needs. Our experienced staff will always be eager to assist you. We look forward to being your reliable business partner when your repossession or locksmith needs arise</p>
    <a class="btn">Read More</a>
  </section>
  <div class="divider"></div>

  <section class="services">
    <h2 class="section-title">Our <span>Services</span></h2>
    <ul class="service-grid">
      <li class="current">Auto keys duplication</li>
      <li>Cutting of new car keys</li>
      <li>Car Lockouts</li>
      <li>Laser key replacement</li>
      <li>Cutting keys by code</li>
      <li>Broken key extractions</li>
      <li>Production of transponder key</li>
      <li>Key fob programming</li>
      <li>Door lock repairs</li>
      <li>Ignition repairs/replacement</li>
    </ul>
  </section>
  <div class="divider"></div>

  <section class="news">
    <h2 class="section-title">Latest <span>News</span></h2>
    <div class="news-grid">
      <article class="news-card">
        <div class="news-head"><div class="date"><b>25</b><small>NOV, 2014</small></div><h3>LOCKSMITH<br>NEWS</h3></div>
        <p>We can now duplicate Kestra, QRT,Ardent and Fellmark keys.</p>
        <a class="more">Read More</a>
      </article>
      <article class="news-card">
        <div class="news-head"><div class="date"><b>15</b><small>NOV, 2014</small></div><h3>LOCKSMITH<br>NEWS</h3></div>
        <p>We can now duplicate Kestra, QRT,Ardent and Fellmark keys.</p>
        <a class="more">Read More</a>
      </article>
      <article class="news-card">
        <div class="news-head"><div class="date"><b>02</b><small>NOV, 2014</small></div><h3>LOCKSMITH<br>NEWS</h3></div>
        <p>We can now duplicate Kestra, QRT,Ardent and Fellmark keys.</p>
        <a class="more">Read More</a>
      </article>
    </div>
  </section>
  <div class="divider"></div>

  <section class="makes">
    <h2 class="section-title">We work on <span>replacement keys</span> for <span>all cars</span></h2>
    <div class="make-grid">
      <div class="make"><i></i>Vorla</div>
      <div class="make"><i></i>Tessin</div>
      <div class="make"><i></i>QRT</div>
      <div class="make"><i></i>Pembrook</div>
      <div class="make"><i></i>Marquenne</div>
      <div class="make"><i></i>Dunmoral</div>
    </div>
  </section>
</main>

<footer class="site-footer">
  <div class="foot-links">Home<span>|</span>About Us<span>|</span>Services<span>|</span>Coverage<span>|</span>Facility<span>|</span>Pricing<span>|</span>Testimonials<span>|</span>FAQ's<span>|</span>Contact Us</div>
  <div class="copy">©2014. Yoursite. All Right Reserved.</div>
  <div class="social"><i></i><i></i><i></i><i></i><i></i></div>
</footer>

</body>
</html>
```